SPA small billboard design and A frame sign

🎨 Creative Designers! We have an exciting opportunity for you! 🎨

Are you passionate about graphic design and have a knack for creating captivating pieces that convey a powerful message? Then this is your chance to shine!

We're seeking a spectacular design for the entrance sign of the prestigious Velora Spa, located within the lush Tamsenko Resort in Puerto Viejo, Costa Rica. This spa offers a unique experience where visitors can indulge in top-notch treatments and combine them with enjoying the resort's facilities, including a credit for the restaurant. It's the perfect oasis for relaxation and rejuvenation!

Project Details:

Entrance Sign: Size 100x64 cm. We want a captivating design that beckons people to enter and experience the luxury and serenity of the Velora Spa.
A-Frame Signs: Two A-frame signs, one to promote the spa's services and the other for spa days. Size 60x80 cm each.

More information about the Velora Spa: Download here: velora.tamsenko-example.com

We're looking for designs that reflect the essence of the Velora Spa and highlight its connection to nature, relaxation, and wellness!

🌟 Ready to be part of this exciting project? Submit your proposals today! 🌟

```html
<!DOCTYPE html>
<html lang="en">
<head>
<meta charset="utf-8">
<title>Velora Spa – Entrance and A-Frame Signs</title>
<link href="https://fonts.googleapis.com/css2?family=Lora:wght@600&family=Poppins:wght@400;500&family=Tinos:wght@700&display=swap" rel="stylesheet">
<style>
  :root{
    --board:#121110;
    --label:#9b9b9b;
    --paper:#ffffff;
    --ink:#151311;
    --teal:#3e7884;
    --orange:#e2892a;
    --navy:#1d4d7c;
    --lilac:#b9a6cf;
    --sky:#dcebfa;
    --mustard:#dfc22f;
    --mint:#cfe8e1;
    --lavender:#e6def3;
    --skin:#d9965c;
    --skin-light:#f0cfae;
    --wood:#b9774a;
  }
  *{box-sizing:border-box;margin:0;padding:0}
  html,body{width:848px;height:1200px;overflow:hidden;background:var(--board)}
  .board{position:relative;width:848px;height:1200px;background:var(--board)}
  .section-title{position:absolute;left:0;width:848px;text-align:center;font-family:"Poppins",sans-serif;font-weight:400;font-size:38px;letter-spacing:8px;color:var(--label)}
  .section-title.entrance{top:30px}
  .section-title.aframe{top:598px}

  /* Entrance sign */
  .entrance-sign{position:absolute;left:66px;top:113px;width:716px;height:458px;background:var(--paper);overflow:hidden}
  .wash{position:absolute}
  .entrance-sign .wash.sky{left:-20px;top:-20px;width:240px;height:120px;background:radial-gradient(ellipse at 35% 35%,var(--sky) 0%,rgba(220,235,250,.7) 45%,transparent 70%)}
  .entrance-sign .wash.mustard{right:-20px;top:-20px;width:240px;height:135px;background:radial-gradient(ellipse at 60% 35%,var(--mustard) 0%,rgba(223,194,47,.85) 40%,transparent 70%)}
  .entrance-sign .wash.mint{left:-20px;bottom:-20px;width:220px;height:160px;background:radial-gradient(ellipse at 35% 65%,var(--mint) 0%,rgba(207,232,225,.75) 45%,transparent 70%)}
  .entrance-sign .wash.lavender{right:-20px;bottom:-20px;width:150px;height:165px;background:radial-gradient(ellipse at 65% 65%,var(--lavender) 0%,rgba(230,222,243,.75) 45%,transparent 70%)}
  .brand-name{position:absolute;left:0;width:100%;text-align:center;font-family:"Lora",serif;font-weight:600;color:var(--ink);line-height:1}
  .entrance-sign .brand-name{top:76px;font-size:210px;letter-spacing:-3px}
  .tagline{position:absolute;left:0;width:100%;text-align:center;font-family:"Poppins",sans-serif;font-weight:500;color:var(--ink);text-transform:uppercase;white-space:nowrap}
  .entrance-sign .tagline{top:282px;font-size:28px;letter-spacing:22px;padding-left:22px}

  /* A-frames */
  .a-frame{position:absolute;top:678px;height:450px;background:var(--paper);overflow:hidden}
  .a-frame.services{left:66px;width:337px}
  .a-frame.hours{left:444px;width:339px}
  .photo{position:absolute}
  .a-frame .brand-name{font-size:24px}
  .a-frame .tagline{font-size:4.5px;letter-spacing:3px}

  .services .photo.massage{left:0;top:0;width:337px;height:320px;
    background:
      radial-gradient(ellipse at 20% 8%,rgba(245,238,246,.95) 0%,rgba(245,238,246,0) 40%),
      radial-gradient(ellipse at 95% 15%,rgba(230,226,224,.9) 0%,rgba(230,226,224,0) 35%),
      linear-gradient(172deg,#ead9cf 0%,#d9a46d 28%,var(--wood) 50%,#c88a5f 64%,#e9d6c9 80%,#f4eef3 100%);
    -webkit-mask-image:linear-gradient(180deg,#000 72%,transparent 100%);
            mask-image:linear-gradient(180deg,#000 72%,transparent 100%)}
  .services .brand-name{left:16px;top:9px;width:auto;text-align:left}
  .services .tagline{left:20px;top:33px;width:auto;text-align:left}
  .services .mist{position:absolute;left:0;bottom:0;width:100%;height:170px;background:
      radial-gradient(ellipse at 25% 80%,rgba(250,244,214,.8) 0%,rgba(250,244,214,0) 50%),
      radial-gradient(ellipse at 80% 20%,rgba(236,230,244,.8) 0%,rgba(236,230,244,0) 50%),
      linear-gradient(180deg,rgba(255,255,255,0),rgba(255,255,255,.9) 14%,#fff 60%,#fbf1d6 100%)}
  .menu-col{position:absolute;top:302px;font-family:"Tinos",serif}
  .menu-col.massages{left:22px}
  .menu-col.treatments{left:186px}
  .menu-col h2{font-size:19px;font-weight:700;color:var(--teal);margin-bottom:4px;line-height:22px}
  .menu-col ul{list-style:none}
  .menu-col li{position:relative;padding-left:10px;height:23.4px}
  .menu-col li::before{content:"";position:absolute;left:0;top:5px;width:3px;height:3px;border-radius:50%;background:var(--orange)}
  .item-name{display:block;font-size:9.4px;font-weight:700;color:var(--orange);line-height:10px}
  .item-price{display:block;font-family:"Poppins",sans-serif;font-size:6.4px;font-weight:500;color:var(--ink);line-height:9px}
  .menu-divider{position:absolute;left:170px;top:304px;width:1px;height:132px;background:var(--lilac)}

  .hours .photo.back-massage{left:0;top:0;width:250px;height:320px;
    background:
      radial-gradient(ellipse at 55% 35%,rgba(240,207,174,.9) 0%,rgba(240,207,174,0) 45%),
      linear-gradient(160deg,#c97a3f 0%,var(--skin) 30%,#e8b58a 55%,var(--skin-light) 72%,#f6ece6 100%);
    -webkit-mask-image:radial-gradient(ellipse 115% 100% at 0% 0%,#000 60%,transparent 100%);
            mask-image:radial-gradient(ellipse 115% 100% at 0% 0%,#000 60%,transparent 100%)}
  .hours .photo.facial{right:0;bottom:0;width:190px;height:190px;
    background:linear-gradient(320deg,#ecd6cc 0%,#f2e1d8 45%,#f8efea 75%);
    -webkit-mask-image:radial-gradient(ellipse 100% 100% at 100% 100%,#000 55%,transparent 100%);
            mask-image:radial-gradient(ellipse 100% 100% at 100% 100%,#000 55%,transparent 100%)}
  .hours .wash.mustard{right:-10px;top:30px;width:140px;height:230px;background:radial-gradient(ellipse at 70% 45%,rgba(223,194,47,.5) 0%,rgba(223,194,47,.22) 45%,transparent 70%)}
  .hours .wash.mint{left:-10px;bottom:-10px;width:170px;height:120px;background:radial-gradient(ellipse at 35% 65%,var(--mint) 0%,rgba(207,232,225,.7) 45%,transparent 70%)}
  .hours .brand-name{top:9px;padding-left:8px}
  .hours .tagline{top:33px;padding-left:12px}
  .hours-title{position:absolute;left:0;width:100%;text-align:center;top:145px;font-family:"Tinos",serif;font-weight:700;font-size:37px;line-height:29px;color:var(--orange)}
  .rule{position:absolute;left:81px;width:169px;height:2px;background:var(--lilac)}
  .rule.first{top:220px}
  .rule.second{top:286px}
  .schedule{position:absolute;left:0;width:100%;text-align:center;font-family:"Tinos",serif;font-weight:700;font-size:21px;line-height:24px;color:var(--navy)}
  .schedule.weekdays{top:228px;padding-left:8px}
  .schedule.weekend{top:295px}
</style>
</head>
<body>
<main class="board">
  <h1 class="section-title entrance">Entrance Sign:</h1>

  <section class="entrance-sign">
    <div class="wash sky" role="img" aria-label="Pale blue brush stroke"></div>
    <div class="wash mustard" role="img" aria-label="Mustard brush stroke"></div>
    <div class="wash mint" role="img" aria-label="Mint brush stroke"></div>
    <div class="wash lavender" role="img" aria-label="Lavender brush stroke"></div>
    <div class="brand-name">velora</div>
    <p class="tagline">Wellness Spa</p>
  </section>

  <h1 class="section-title aframe">A-Frame Signs:</h1>

  <section class="a-frame services">
    <div class="photo massage" role="img" aria-label="Therapist giving a back massage in a spa room"></div>
    <div class="mist"></div>
    <div class="brand-name">velora</div>
    <p class="tagline">Wellness Spa</p>

    <div class="menu-col massages">
      <h2>Massages</h2>
      <ul>
        <li><span class="item-name">Masaje Con CBD</span><span class="item-price">60 min $79 USD</span></li>
        <li><span class="item-name">Masaje De Tejido Profundo</span><span class="item-price">60 min $89 USD | 90 min $109 USD</span></li>
        <li><span class="item-name">Masaje Relajante</span><span class="item-price">60 min $75 USD | 90 min $99 USD</span></li>
        <li><span class="item-name">Masaje Con Piedras Calientes</span><span class="item-price">60 min $75 USD | 90 min $99 USD</span></li>
        <li><span class="item-name">Masaje Con Chocolate</span><span class="item-price">60 min $79 USD</span></li>
      </ul>
    </div>
    <div class="menu-divider"></div>
    <div class="menu-col treatments">
      <h2>Treatments</h2>
      <ul>
        <li><span class="item-name">Exfoliacion Velora</span><span class="item-price">60 min $79 USD | 90 min $99 USD</span></li>
        <li><span class="item-name">Cuidado Post Sol</span><span class="item-price">60 min $79 USD</span></li>
        <li><span class="item-name">Facial Vive El Caribe</span><span class="item-price">60 min $65 USD</span></li>
        <li><span class="item-name">Manicura Velora</span><span class="item-price">básico $40</span></li>
        <li><span class="item-name">Pedicura Velora</span><span class="item-price">básico $50</span></li>
      </ul>
    </div>
  </section>

  <section class="a-frame hours">
    <div class="wash mustard" role="img" aria-label="Mustard brush stroke"></div>
    <div class="photo back-massage" role="img" aria-label="Woman relaxing during a shoulder massage"></div>
    <div class="photo facial" role="img" aria-label="Guest receiving a facial mask treatment"></div>
    <div class="wash mint" role="img" aria-label="Mint brush stroke"></div>
    <div class="brand-name">velora</div>
    <p class="tagline">Wellness Spa</p>
    <h2 class="hours-title">Opening<br>hours</h2>
    <div class="rule first"></div>
    <p class="schedule weekdays">Monday to Friday<br>9 AM - 8 PM</p>
    <div class="rule second"></div>
    <p class="schedule weekend">Saturday &amp; Sunday<br>10 AM - 8 PM</p>
  </section>
</main>
</body>
</html>
```